Fennick Executive Search - New Business Card Design Project

We are an executive search firm called Fennick Executive Search based in the UK. We require a custom design for a business card. We're looking to convey a professional service to executives for executive search recruitment services. In terms of colours, we like dark blues and grays (maybe even silver incorporated somewhere if we go for a foiled type of card) but we're open to your artistic flare. See our current logo in attachments. We are totally open on design so long as the design is slick and professional.
Updates

Thanks for all your contributions of various designs. I have to say the quality of work has been amazing which is going to make our job quite difficult in the coming days on making a decision. Thanks to you all that have taken the time to submit designs thus far. We'll keep on reviewing and try to narrow down our selection as soon as possible.

Target Market(s)

Executive Search

Industry/Entity Type

Recruitment

Contact Information for Business Card

Fennick Executive Search,
Exclusively Sourcing & Hiring Senior Leaders
Gordon Pellbury, Managing Director,
07823 906417
0117 486 7132
gordon@fennickexecutive.co.uk
fennickexecutive.co.uk
58 Lindmoor Court, Hatherley Road, Bristol, BS32 9QJ

Font styles to use
Sans Serif
Other font styles liked:
• Roboto (which is used in our logo)

Requirements
Must have
• Our logo (It has a subtle fade on it from #02071d at top to #333649 at bottom)
• The logo can be on one side or both sides
• Must be elegant and professional
• We have 2nd slogan CONSULT | INSPIRE | INNOVATE | DELIVER which can be incorporated into the card
Nice to have
• Use of blues and grey colours
• Compatible with similar styling to our website fennickexecutive.co.uk
Should not have
• Must not be overly brash
• Must not contain cartoon characters

```html
<!DOCTYPE html>
<html lang="en">
<head>
<meta charset="utf-8">
<title>Fennick Executive Search – Business Card</title>
<link href="https://fonts.googleapis.com/css2?family=Roboto:ital,wght@0,400;0,500;0,700;1,700&display=swap" rel="stylesheet">
<style>
  :root {
    --stage: #9a9a9a;
    --paper: #ffffff;
    --navy-top: #1b1f33;
    --navy-bottom: #373a4d;
    --navy-flat: #2a2d40;
    --navy-text: #1e3a5f;
    --name-blue: #1d3f6e;
    --grey-text: #5a5a5a;
    --frame-grey: #8a8a8a;
    --bar-grey: #dcdcdc;
    --icon-grey: #6f7480;
  }
  * { margin: 0; padding: 0; box-sizing: border-box; }
  html, body { width: 1200px; height: 1200px; overflow: hidden; }
  body {
    background: var(--stage);
    font-family: "Roboto", Arial, sans-serif;
    display: flex;
    flex-direction: column;
    align-items: center;
    justify-content: center;
    gap: 50px;
  }
  .card {
    position: relative;
    width: 800px;
    height: 530px;
    box-shadow: 0 6px 18px rgba(0,0,0,.35);
    overflow: hidden;
  }
  .card__frame {
    position: absolute;
    inset: 13px;
    border: 1.5px solid var(--frame-grey);
    pointer-events: none;
  }

  /* Front */
  .card--front { background: var(--paper); }
  .logo-placeholder {
    position: absolute;
    left: 30px; top: 28px;
    width: 163px; height: 163px;
    background: var(--navy-flat);
  }
  .tagline {
    position: absolute;
    right: 40px; top: 26px;
    font-size: 18px;
    font-weight: 700;
    letter-spacing: .4px;
    color: var(--grey-text);
  }
  .person {
    position: absolute;
    right: 40px; top: 128px;
    text-align: right;
  }
  .person__name {
    font-size: 32px;
    line-height: 38px;
    color: var(--name-blue);
    letter-spacing: .6px;
    font-weight: 400;
  }
  .person__name b { font-weight: 700; }
  .person__role {
    margin-top: 4px;
    font-size: 16px;
    font-weight: 700;
    color: var(--grey-text);
    letter-spacing: .8px;
  }
  .edge-tab { position: absolute; background: linear-gradient(180deg, var(--navy-top), var(--navy-bottom)); }
  .edge-tab--right { right: 0; top: 130px; width: 16px; height: 78px; }
  .edge-tab--left { left: 0; top: 288px; width: 14px; height: 214px; }
  .contacts { position: absolute; left: 24px; top: 289px; width: 756px; list-style: none; }
  .contact {
    display: flex;
    align-items: center;
    height: 36px;
    margin-bottom: 21px;
    background: linear-gradient(90deg, var(--bar-grey) 0%, #ececec 60%, rgba(255,255,255,0) 100%);
    color: var(--navy-text);
    font-size: 21px;
  }
  .contact:last-child { margin-top: 6px; margin-bottom: 0; }
  .contact svg { width: 26px; height: 26px; margin: 0 14px 0 8px; flex: none; }

  /* Back */
  .card--back { background: linear-gradient(180deg, var(--navy-top), var(--navy-bottom)); color: #fff; }
  .card--back .card__frame { border-color: rgba(255,255,255,.75); inset: 15px; }
  .company-name { position: absolute; left: 72px; top: 176px; font-weight: 500; line-height: 1.08; }
  .company-name__main { display: block; font-size: 54px; letter-spacing: 1px; }
  .company-name__sub { display: block; font-size: 28px; }
  .divider { position: absolute; left: 400px; top: 181px; width: 2px; height: 92px; background: #fff; }
  .back-url { position: absolute; left: 440px; top: 212px; font-size: 20px; letter-spacing: .5px; }
  .slogan {
    position: absolute;
    left: 100px; top: 336px;
    width: 602px;
    text-align: center;
    font-size: 29px;
    font-style: italic;
    font-weight: 700;
    letter-spacing: 1px;
    padding-bottom: 8px;
    border-bottom: 2px solid rgba(255,255,255,.85);
  }
</style>
</head>
<body>

<section class="card card--front" aria-label="Business card front">
  <div class="card__frame"></div>
  <div class="logo-placeholder" role="img" aria-label="Fennick Executive Search logo"></div>
  <p class="tagline">EXCLUSIVELY SOURCING &amp; HIRING SENIOR LEADERS</p>
  <div class="person">
    <p class="person__name"><b>GORDON</b> PELLBURY</p>
    <p class="person__role">MANAGING DIRECTOR</p>
  </div>
  <div class="edge-tab edge-tab--right"></div>
  <div class="edge-tab edge-tab--left"></div>
  <ul class="contacts">
    <li class="contact">
      <svg viewBox="0 0 28 28" aria-hidden="true"><rect x="1" y="1" width="26" height="26" rx="5" fill="#fff" stroke="var(--icon-grey)" stroke-width="1.5"/><path d="M9 7c1-1 2 0 3 2s0 2-1 3c1 2 3 4 5 5 1-1 1-2 3-1s3 2 2 3c-1 2-3 2-5 1-4-2-7-5-8-9-1-2 0-3 1-4z" fill="var(--icon-grey)"/></svg>
      07823 906417 / 0117 486 7132
    </li>
    <li class="contact">
      <svg viewBox="0 0 28 28" aria-hidden="true"><rect x="1" y="1" width="26" height="26" rx="5" fill="#fff" stroke="var(--icon-grey)" stroke-width="1.5"/><rect x="6" y="8.5" width="16" height="11" fill="none" stroke="var(--icon-grey)" stroke-width="1.5"/><path d="M6 8.5l8 6 8-6" fill="none" stroke="var(--icon-grey)" stroke-width="1.5"/></svg>
      gordon@fennickexecutive.co.uk
    </li>
    <li class="contact">
      <svg viewBox="0 0 28 28" aria-hidden="true"><rect x="1" y="1" width="26" height="26" rx="5" fill="#fff" stroke="var(--icon-grey)" stroke-width="1.5"/><g fill="none" stroke="var(--icon-grey)" stroke-width="1.3"><circle cx="14" cy="14" r="8"/><ellipse cx="14" cy="14" rx="3.5" ry="8"/><path d="M6 14h16M7.5 10h13M7.5 18h13"/></g></svg>
      fennickexecutive.co.uk
    </li>
    <li class="contact">
      <svg viewBox="0 0 28 28" aria-hidden="true"><rect x="1" y="1" width="26" height="26" rx="5" fill="#fff" stroke="var(--icon-grey)" stroke-width="1.5"/><path d="M14 23s-6-7-6-11a6 6 0 0 1 12 0c0 4-6 11-6 11z" fill="var(--icon-grey)"/><circle cx="14" cy="12" r="2.3" fill="#fff"/></svg>
      58 Lindmoor Court, Hatherley Road, Bristol, BS32 9QJ
    </li>
  </ul>
</section>

<section class="card card--back" aria-label="Business card back">
  <div class="card__frame"></div>
  <p class="company-name">
    <span class="company-name__main">FENNICK</span>
    <span class="company-name__sub">EXECUTIVE SEARCH</span>
  </p>
  <div class="divider"></div>
  <p class="back-url">FENNICKEXECUTIVE.CO.UK</p>
  <p class="slogan">CONSULT | INSPIRE | INNOVATE | DELIVER</p>
</section>

</body>
</html>
```